Miel (Honey) Label for Marlow Brook Farm, Temecula Valley, CA

A label design for bottles of freshly harvested natural honey. I've included a picture of the bottles being used. They are 16 oz, plastic bottles. The bee hives are on a farm in Temecula Valley (Wine Country), CA. The name of the farm is Marlow Brook Farm. Marlow Brook Farm specializes in breeding Thoroughbred horses for racing, and equestrian sports of Hunter & Competition Jumping. The owners of the farm are originally from Geneva, Switzerland with their native language being French. I'd like the label to reflect the 3 things - horses, bees/honey, & France. Instead of using the word "honey" on the label, I'd like the word Miel used to include the owners French background. Miel means honey in French. The label should have a Country French look. The words that come to my mind to explain what I'm looking for are: Vintage, Edwin Carrow, Linen Hutch, Organic, Natural. To include a Fleur de lis somewhere in the design would be a nice representation of the owners French heritage.

The plastic containers being used to package the honey at this time Measures 5-1/4-inch height ( Up and down ) by 3-1/2-inch width
(Across) x 1-3/4-inch thick. I provided a sample picture of the bottle in my images. It's the Greta's Meadow Honey image I posted on Monday. Please let me know if you have any questions.

Target Market(s)

Natural Food Enthusiasts; Foodies; Millennials; Trendy & hip people from LA coming to the Temecula Valley to go wine tasting. Think Dorset Lane/Venice Beach/ Silverlake, CA. Also, well established, down to earth, sophisticated people with "old" money. Equestrian Sports Enthusiasts of horse racing, English Riding, & Hunter/Jumping. Equestrian Sports are considered and referred to as "the sport of Kings". Farm to table enthusiasts.

Industry/Entity Type

Plastic

Font styles to use
Decorative
Script
Other font styles liked:
• snell Round Bold; Century Gothic; Sans Serif

Colors

Designer to choose colors to be used in the design.

Requirements
Must have
• The name: Marlow Brook Farm somewhere on the label.
• Horses - Silhouettes of thoroughbred horse Hunter Jumping (possibly racing). (See samples of images I pulled from the internet.)
• Bee hives/honey bees/honey
• Honey written in French - Miel
• Country French - Rustic, Simple, but elegant.
Nice to have
• Fleur de lis. Country French & Industrial tone. Trendy & cool with a natural, down to earth feel. A wow factor that draws a person to it.
• Produced in Temecula Valley Wine Country, CA
• Country French/Country Italian/ Romantic/European
Should not have
• Multiple colors. Overly busy. Print too small to read or too ornate to comfortably read.

```html
<!DOCTYPE html>
<html lang="en">
<head>
<meta charset="utf-8">
<title>Marlow Brook Farms Miel Label</title>
<link rel="stylesheet" href="https://fonts.googleapis.com/css2?family=Playfair+Display:wght@700&family=Parisienne&family=Courier+Prime&family=Open+Sans:wght@400;600&display=swap">
<style>
  :root {
    --page: #ffffff;
    --label-cream: #efece4;
    --ink: #141414;
    --placeholder: #2a2a2a;
  }
  * { margin: 0; padding: 0; box-sizing: border-box; }
  html, body {
    width: 1200px;
    height: 900px;
    overflow: hidden;
    background: var(--page);
  }
  .canvas {
    position: relative;
    width: 1200px;
    height: 900px;
  }
  .label {
    position: absolute;
    left: 239px;
    top: 158px;
    width: 722px;
    height: 584px;
    color: var(--ink);
  }
  .label-frame {
    position: absolute;
    inset: 0;
  }
  .label-content {
    position: absolute;
    inset: 0;
  }
  .brand-mark {
    position: absolute;
    top: 34px;
    left: 0;
    right: 0;
    display: flex;
    align-items: center;
    justify-content: center;
    gap: 10px;
  }
  .brand-mark-circle {
    width: 30px;
    height: 30px;
    border: 2px solid var(--ink);
    border-radius: 50%;
  }
  .brand-mark-name {
    font-family: "Open Sans", sans-serif;
    font-weight: 600;
    font-size: 17px;
    letter-spacing: 0.08em;
    text-transform: uppercase;
  }
  .horse-silhouettes {
    position: absolute;
    top: 118px;
    left: 271px;
    width: 180px;
    height: 64px;
    background: var(--placeholder);
    border-radius: 6px;
  }
  .farm-script {
    position: absolute;
    top: 186px;
    left: 0;
    right: 0;
    text-align: center;
    font-family: "Parisienne", cursive;
    font-size: 44px;
    line-height: 1;
  }
  .rule {
    position: absolute;
    left: 149px;
    width: 424px;
    height: 2px;
    background: var(--ink);
  }
  .rule-top { top: 252px; }
  .rule-bottom { top: 408px; }
  .product-name {
    position: absolute;
    top: 256px;
    left: 0;
    right: 0;
    text-align: center;
    font-family: "Playfair Display", serif;
    font-weight: 700;
    font-size: 162px;
    line-height: 1;
    letter-spacing: 0.02em;
  }
  .product-tagline {
    position: absolute;
    top: 422px;
    left: 0;
    right: 0;
    text-align: center;
    font-family: "Courier Prime", monospace;
    font-size: 25px;
    letter-spacing: 0.04em;
  }
  .label-footer {
    position: absolute;
    top: 488px;
    left: 66px;
    right: 66px;
    height: 80px;
    display: flex;
    align-items: center;
    justify-content: space-between;
    font-family: "Open Sans", sans-serif;
    font-size: 15px;
  }
  .footer-ornament {
    width: 104px;
    height: 70px;
    background: var(--placeholder);
    border-radius: 8px;
  }
</style>
</head>
<body>
  <main class="canvas">
    <section class="label">
      <svg class="label-frame" width="722" height="584" viewBox="0 0 722 584" aria-hidden="true">
        <path d="M0,584 L0,290 C0,100 180,0 361,0 C542,0 722,100 722,290 L722,584 Z" fill="var(--label-cream)"/>
        <path d="M8,576 L8,290 C8,106 184,8 361,8 C538,8 714,106 714,290 L714,576 Z" fill="none" stroke="var(--ink)" stroke-width="6"/>
        <path d="M18,566 L18,290 C18,113 189,18 361,18 C533,18 704,113 704,290 L704,566 Z" fill="none" stroke="var(--ink)" stroke-width="1.5"/>
      </svg>
      <div class="label-content">
        <div class="brand-mark">
          <span class="brand-mark-circle"></span>
          <span class="brand-mark-name">Marlow Brook Farm</span>
        </div>
        <div class="horse-silhouettes" role="img" aria-label="Silhouette of a grazing mare and her foal"></div>
        <p class="farm-script">Marlow Brook Farms</p>
        <div class="rule rule-top"></div>
        <h1 class="product-name">MIEL</h1>
        <div class="rule rule-bottom"></div>
        <p class="product-tagline">pure and natural honey</p>
        <div class="label-footer">
          <span class="origin">Temecula Valley, California</span>
          <span class="footer-ornament" role="img" aria-label="Symmetrical fleur-de-lis scroll ornament"></span>
          <span class="net-weight">Net Weight 16 oz (454 gm)</span>
        </div>
      </div>
    </section>
  </main>
</body>
</html>
```